Vesprine Oakville Cabernet Sauvignon-Wine label design

We need a package design for an up market wine brand named, Vesprine. It will be a Cabernet Sauvignon from the Oakville AVA of Napa Valley. We are looking for a stylish modern label that will stand out on a retail shelf. We want the label to be attention grabbing and stylish while presenting an up market luxury brand.

Sick

Requirements
Must have
• Must have the words(in order of importance)
-Vesprine
-Cabernet Sauvignon
-Oakville
-Napa Valley
-2018

Must be designed for a traditional "Bordeaux" style bottle (Bottle specs in uploaded files)
Should not have
• Any images of grapes, vineyards, wine glasses or bottles

```html
<!DOCTYPE html>
<html lang="en">
<head>
<meta charset="utf-8">
<title>Vesprine Cabernet Sauvignon – Label</title>
<link href="https://fonts.googleapis.com/css2?family=Figtree:wght@600;800&display=swap" rel="stylesheet">
<style>
  :root {
    --backdrop: #f1f1f1;
    --wine-bright: #a21d36;
    --wine-mid: #7a2230;
    --wine-deep: #2f1620;
    --paper-grey: #d5d7d7;
    --brand-pink: #c62350;
    --brand-mauve: #7d5560;
    --vintage: #3f1d21;
    --ink-light: #ffffff;
  }
  html, body {
    margin: 0;
    padding: 0;
    width: 1200px;
    height: 1200px;
    overflow: hidden;
    background: var(--backdrop);
  }
  .canvas {
    position: relative;
    width: 1200px;
    height: 1200px;
  }
  .wine-label {
    position: absolute;
    left: 293px;
    top: 50px;
    width: 613px;
    height: 1101px;
    display: block;
  }
  .brand-name {
    font-family: "Figtree", sans-serif;
    font-weight: 800;
    font-size: 210px;
  }
  .vintage {
    font-family: "Figtree", sans-serif;
    font-weight: 800;
    font-size: 218px;
    fill: var(--vintage);
  }
  .details {
    font-family: "Figtree", sans-serif;
    font-weight: 600;
    font-size: 27px;
    fill: var(--ink-light);
  }
</style>
</head>
<body>
<main class="canvas">
  <svg class="wine-label" viewBox="0 0 613 1101" xmlns="http://www.w3.org/2000/svg" aria-label="Vesprine 2018 Cabernet Sauvignon, Oakville, Napa Valley">
    <defs>
      <radialGradient id="label-field" cx="0.05" cy="0.05" r="1.15">
        <stop offset="0" stop-color="var(--wine-bright)"/>
        <stop offset="0.45" stop-color="var(--wine-mid)"/>
        <stop offset="1" stop-color="var(--wine-deep)"/>
      </radialGradient>
      <linearGradient id="brand-fade" x1="0" y1="0" x2="0" y2="1">
        <stop offset="0" stop-color="var(--brand-pink)"/>
        <stop offset="1" stop-color="var(--brand-mauve)"/>
      </linearGradient>
    </defs>

    <rect class="label-base" width="613" height="1101" fill="var(--paper-grey)"/>
    <path class="label-field" d="M0,0 H613 V830 C500,1000 380,1101 225,1101 C130,1101 50,1070 0,1040 Z" fill="url(#label-field)"/>

    <text class="brand-name" fill="url(#brand-fade)" transform="translate(58,86) rotate(90)" x="0" y="0" textLength="917" lengthAdjust="spacingAndGlyphs" dominant-baseline="auto">VESPRINE</text>

    <text class="vintage" x="230" y="595" textLength="372" lengthAdjust="spacingAndGlyphs">2018</text>

    <text class="details" x="229" y="855">CABERNET</text>
    <text class="details" x="229" y="894">SAUVIGNON</text>
    <line class="details-rule" x1="229" y1="919" x2="424" y2="919" stroke="var(--ink-light)" stroke-width="2"/>
    <text class="details" x="229" y="969">OAKVILLE</text>
    <text class="details" x="229" y="1008">NAPA VALLEY</text>
  </svg>
</main>
</body>
</html>
```